Bright Haven Estate Sales web design

We are looking to launch an Estate Sales Website for Nashville, TN. The name of our Business is Bright Haven Estate Sales. We would like to give you a blank slate so that you can showcase your design skills for us. The few things we are looking for are a nice header graphic of a house or a stock image of an estate sale. Near the header graphic we would like a quick inquiry form. If not on the right side of the header maybe midway down the site. We potentially want to see what purple and Gold look like on the site however this is not a must. We have over 20 years of industry related experience.

1. Buttons at top of the website will be.
a. Services
b. Upcoming Sales
c. About Us
d. FAQs
e. Resources

Services we offer:
1. Estate Sales
2. Cleanouts
3. Appraisals

Sites We like:
https://www.corvellestatesales.example/

We don't have a logo yet so if you have ideas please share them with us. Below are 2 ideas however if you have your own thoughts please ignore.

1. Oval ornate frame, gold and black, with BHES in the middle, deep purple. Think of catering to high class people..font should be fancy as opposed to simple.

2. Another option, Bright Haven in bold fancy script, same colors, with Estate Sales below, small different font, black.

```html
<!DOCTYPE html>
<html lang="en">
<head>
<meta charset="utf-8">
<title>Bright Haven Estate Sales</title>
<link href="https://fonts.googleapis.com/css2?family=Montserrat:wght@400;500;600;700&family=Pinyon+Script&display=swap" rel="stylesheet">
<style>
:root{
  --gold:#c99a33;
  --gold-dark:#b7872a;
  --cream:#fdf3df;
  --ink:#1d1d1d;
  --muted:#7a7a7a;
  --white:#ffffff;
  --line:#9a9a9a;
  --night:#0b0b0b;
}
*{box-sizing:border-box;margin:0;padding:0}
html,body{width:1200px;height:4677px;overflow:hidden}
body{position:relative;background:var(--white);font-family:'Montserrat',sans-serif;color:var(--ink)}
.abs{position:absolute}
.script{font-family:'Pinyon Script',cursive;font-weight:400;color:var(--ink)}
.btn{position:absolute;display:flex;align-items:center;justify-content:center;background:var(--gold);color:var(--white);font-weight:600;border-radius:30px;font-size:15px}
.center{text-align:center}

/* header */
.site-header{position:absolute;left:0;top:0;width:1200px;height:84px;background:var(--cream);z-index:5}
.brand-tab{position:absolute;left:109px;top:0;width:172px;height:113px;background:var(--white);border-radius:0 0 14px 14px;box-shadow:0 4px 10px rgba(0,0,0,.15);display:flex;flex-direction:column;align-items:center;justify-content:center;z-index:6;font-weight:600;font-size:15px;line-height:1.3;text-align:center;color:var(--ink)}
.nav a{position:absolute;top:34px;font-size:13px;font-weight:500;color:var(--ink);text-decoration:none;letter-spacing:.3px}
.contact-btn{left:940px;top:18px;width:144px;height:46px}

/* hero */
.hero-photo{position:absolute;left:0;top:84px;width:1200px;height:600px;background:linear-gradient(160deg,#3e4a3a 0%,#6f7a72 35%,#b8b4ad 55%,#5b5e4e 80%,#2f3a28 100%)}
.hero-shade{position:absolute;left:0;top:84px;width:1200px;height:600px;background:rgba(0,0,0,.35)}
.hero-title-small{left:0;width:1200px;top:200px;font-size:46px;color:var(--white)}
.hero-title{left:0;width:1200px;top:258px;font-size:60px;color:var(--white)}
.hero-frame{left:296px;top:297px;width:604px;height:118px;border:4px solid var(--gold);border-top:none;border-radius:0 0 10px 10px}
.hero-frame-top{top:294px;height:4px;background:var(--gold)}
.hero-copy{left:350px;width:500px;top:338px;font-size:13.5px;line-height:26px;color:var(--white)}

/* enquiry */
.enquiry{left:102px;top:545px;width:996px;height:511px;background:var(--white);border-radius:6px;box-shadow:0 4px 14px rgba(0,0,0,.14)}
.enquiry h2{position:absolute;left:0;width:996px;top:30px;text-align:center;font-size:50px}
.field-label{position:absolute;font-size:15px;font-weight:500}
.field{position:absolute;border:1.5px solid var(--line);border-radius:8px;font-size:12px;padding:0 12px;display:flex;align-items:center}
.field.area{align-items:flex-start;padding-top:12px}

/* services */
.section-title{position:absolute;left:0;width:1200px;text-align:center;font-size:54px}
.service-photo{position:absolute;top:1223px;width:309px;height:265px}
.service-card{position:absolute;top:1425px;width:276px;height:240px;background:var(--white);border-radius:140px 140px 0 0/40px 40px 0 0;border-top:4px solid var(--gold);box-shadow:0 6px 12px rgba(0,0,0,.12);text-align:center}
.service-card h3{margin-top:62px;font-size:20px;font-weight:500}
.service-card p{margin:14px auto 0;width:220px;font-size:13px;line-height:26px;color:var(--muted)}
.service-card a{display:block;margin-top:2px;font-size:13px;font-weight:600;color:var(--gold);text-decoration:underline}
.service-icon{position:absolute;top:10px;right:14px;width:44px;height:44px;border-radius:50%;background:var(--cream);display:flex;align-items:center;justify-content:center}

/* about */
.about-photo{position:absolute;left:0;top:1743px;width:1200px;height:672px;background:linear-gradient(180deg,#1f3d8c 0%,#2c4fa4 40%,#3d4f78 70%,#1b2540 100%)}
.about-card{left:111px;top:1851px;width:976px;height:458px;background:rgba(255,255,255,.9);border-radius:6px}
.about-card h2{position:absolute;left:0;width:976px;top:30px;text-align:center;font-size:54px}
.about-copy{position:absolute;left:110px;width:756px;top:108px;font-size:13px;line-height:26px;color:var(--muted);text-align:center}
.stats{position:absolute;left:218px;top:236px;width:539px;height:82px;background:var(--white);border-radius:4px;box-shadow:0 3px 8px rgba(0,0,0,.2);display:flex}
.stat{flex:1;display:flex;align-items:center;gap:16px;padding-left:26px;font-size:14px;line-height:24px}
.stat+.stat{border-left:1.5px solid #d5d5d5}

/* resources */
.res-title{left:111px;top:2490px;font-size:56px}
.res-copy{left:111px;top:2574px;width:440px;font-size:13.5px;line-height:25.8px;color:var(--muted)}

/* upcoming */
.upcoming-band{position:absolute;left:0;top:2964px;width:1200px;height:640px;background:linear-gradient(180deg,#fbeed6 0%,#fdf5e6 55%,#f7e5bd 100%)}
.sale-card{position:absolute;top:3142px;height:356px;background:var(--white);border-radius:6px;box-shadow:0 2px 8px rgba(0,0,0,.1);overflow:hidden}
.sale-photo{position:absolute;left:6px;top:6px;right:6px;height:232px;border-radius:4px}
.sale-card p{position:absolute;left:16px;top:254px;width:420px;font-size:17px;line-height:29px;font-weight:500}
.sale-card a{position:absolute;left:18px;top:316px;font-size:15px;font-weight:600;color:var(--gold);display:flex;align-items:center;gap:8px;text-decoration:none}

/* faq */
.faq-item{position:absolute;left:185px;width:828px;background:var(--white);box-shadow:0 2px 8px rgba(0,0,0,.18);border-radius:3px}
.faq-q{height:55px;display:flex;align-items:center;justify-content:space-between;padding:0 18px;font-size:15px;font-weight:500}
.faq-q span.sign{font-size:26px;font-weight:500}
.faq-a{padding:0 18px 18px 20px;margin-top:-8px;font-size:13px;line-height:26px;color:var(--muted)}

/* footer */
.footer{position:absolute;left:0;top:4293px;width:1200px;height:384px;background:var(--night);color:var(--white)}
.foot-brand{position:absolute;left:105px;top:68px;width:200px;height:146px;display:flex;align-items:center;justify-content:center;text-align:center;font-size:19px;font-weight:600;line-height:1.35;color:var(--gold)}
.foot-col h4{position:absolute;top:50px;font-size:20px;font-weight:500}
.foot-link{position:absolute;font-size:13px}
.subscribe{left:891px;top:41px;width:198px;height:236px;background:var(--gold);border-radius:4px;text-align:center}
.subscribe h4{margin-top:32px;font-size:22px;font-weight:500}
.subscribe p{margin:12px auto 0;width:160px;font-size:12px;line-height:27px}
.sub-input{margin:14px auto 0;width:162px;height:36px;border:1.5px solid var(--white);border-radius:20px;display:flex;align-items:center;justify-content:space-between;padding:0 4px 0 10px;font-size:9.5px}
.foot-rule{position:absolute;left:111px;top:314px;width:978px;height:1.5px;background:#8a8a8a}
.social{position:absolute;top:330px;width:34px;height:34px;border:1.5px solid var(--white);border-radius:50%}
.copyright{position:absolute;right:111px;top:338px;font-size:13px}
</style>
</head>
<body>

<header class="site-header">
  <nav class="nav">
    <a style="left:396px">SERVICES</a>
    <a style="left:496px">UPCOMING SALES</a>
    <a style="left:648px">ABOUT US</a>
    <a style="left:751px">FAQS</a>
    <a style="left:821px">RESOURCES</a>
  </nav>
  <div class="btn contact-btn">Contact Us</div>
</header>
<div class="brand-tab">Bright Haven<br>Estate Sales</div>

<!-- hero -->
<div class="hero-photo" role="img" aria-label="Modern two-storey house with dark roof among green trees"></div>
<div class="hero-shade"></div>
<svg class="abs" style="left:0;top:560px" width="1200" height="130" viewBox="0 0 1200 130"><path d="M0 110 Q600 0 1200 110 L1200 130 L0 130Z" fill="#fff"/></svg>
<div class="abs script center hero-title-small">Welcome To</div>
<div class="abs script center hero-title">Bright Haven Estate Sales</div>
<div class="abs hero-frame"></div>
<div class="abs hero-frame-top" style="left:296px;width:56px"></div>
<div class="abs hero-frame-top" style="left:846px;width:54px"></div>
<p class="abs center hero-copy">Lorem Ipsum is simply dummy text of the printing and typesetting industry. Lorem Ipsum has been the industry's standard dummy text ever since the 1500s, when an unknown printer took a galley of type</p>
<div class="btn" style="left:526px;top:437px;width:144px;height:42px">Get Started</div>

<!-- enquiry -->
<section class="abs enquiry">
  <h2 class="script">Quick Enquiry</h2>
  <div class="field-label" style="left:47px;top:104px">Name</div>
  <div class="field" style="left:41px;top:130px;width:294px;height:46px">John Doe</div>
  <div class="field-label" style="left:359px;top:104px">Phone Number</div>
  <div class="field" style="left:352px;top:130px;width:296px;height:46px">+1888 888 8888</div>
  <div class="field-label" style="left:670px;top:104px">Email</div>
  <div class="field" style="left:664px;top:130px;width:294px;height:46px">info@abc.com</div>
  <div class="field-label" style="left:47px;top:193px">Current Address</div>
  <div class="field" style="left:41px;top:219px;width:607px;height:46px">123 Lorem Ipsum</div>
  <div class="field-label" style="left:670px;top:193px">Zip Code</div>
  <div class="field" style="left:664px;top:219px;width:294px;height:46px">90224</div>
  <div class="field-label" style="left:47px;top:281px">Comment</div>
  <div class="field area" style="left:41px;top:308px;width:917px;height:88px">Type Here</div>
  <div class="btn" style="left:412px;top:421px;width:176px;height:45px">Submit</div>
</section>

<!-- services -->
<h2 class="section-title script" style="top:1122px">Our Services</h2>
<div class="service-photo" style="left:114px;background:linear-gradient(135deg,#8b5a4a,#c9a48c 50%,#6e6a62)" role="img" aria-label="Miniature house models with a red upward arrow"></div>
<div class="service-photo" style="left:445px;background:linear-gradient(135deg,#1f2a44,#c79a6d 55%,#3b3b44)" role="img" aria-label="Hands passing a house key"></div>
<div class="service-photo" style="left:779px;background:linear-gradient(135deg,#d9d4cc,#f1ede7 50%,#a58b78)" role="img" aria-label="Model house beside papers and a calculator"></div>

<div class="service-card" style="left:131px">
  <div class="service-icon"><svg width="26" height="26" viewBox="0 0 24 24" fill="none" stroke="#1d1d1d" stroke-width="1.8"><path d="M3 11l9-7 9 7"/><path d="M5 10v10h14V10"/><path d="M10 20v-6h4v6"/></svg></div>
  <h3>Estate Sales</h3>
  <p>Lorem Ipsum is simply dummy text of the printing and typesetting industry. Lorem Ipsum has been the industry's</p>
  <a>Read More..</a>
</div>
<div class="service-card" style="left:462px">
  <div class="service-icon"><svg width="26" height="26" viewBox="0 0 24 24" fill="none" stroke="#1d1d1d" stroke-width="1.6"><path d="M10 3l2 6 6 2-6 2-2 6-2-6-6-2 6-2z"/><path d="M19 2v4M17 4h4M19 17v4M17 19h4"/></svg></div>
  <h3>Cleanouts</h3>
  <p>Lorem Ipsum is simply dummy text of the printing and typesetting industry. Lorem Ipsum has been the industry's</p>
  <a>Read More..</a>
</div>
<div class="service-card" style="left:795px">
  <div class="service-icon"><svg width="26" height="26" viewBox="0 0 24 24" fill="none" stroke="#1d1d1d" stroke-width="1.6"><path d="M5 3h10l4 4v14H5z"/><path d="M8 9h8M8 13h6M8 17h4"/><circle cx="17" cy="18" r="3"/></svg></div>
  <h3>Appraisals</h3>
  <p>Lorem Ipsum is simply dummy text of the printing and typesetting industry. Lorem Ipsum has been the industry's</p>
  <a>Read More..</a>
</div>

<!-- about -->
<div class="about-photo" role="img" aria-label="Modern villa with pool lit at dusk"></div>
<svg class="abs" style="left:0;top:1735px" width="1200" height="90" viewBox="0 0 1200 90"><path d="M0 0 H1200 V60 Q600 -20 0 60Z" fill="#fff"/><path d="M40 40 Q600 -18 1160 40" stroke="#c99a33" stroke-width="5" fill="none"/></svg>
<section class="abs about-card">
  <h2 class="script">About Us</h2>
  <p class="about-copy">Lorem Ipsum is simply dummy text of the printing and typesetting industry. Lorem Ipsum has been the industry's standard dummy text ever since the 1500s, when an unknown printer took a galley of type and scrambled it to make a type specimen book. It has survived not only five centuries, but also the leap into electronic typesetting, remaining essentially unchanged.Lorem Ipsum is simply dummy text of the printing</p>
  <div class="stats">
    <div class="stat"><svg width="48" height="42" viewBox="0 0 48 42" fill="#c99a33"><rect x="2" y="14" width="18" height="26" rx="2"/><rect x="24" y="20" width="22" height="20" rx="2"/><circle cx="36" cy="9" r="6"/></svg><span>20 years of industry<br>related experience</span></div>
    <div class="stat"><svg width="52" height="42" viewBox="0 0 52 42" fill="#c99a33"><circle cx="14" cy="20" r="5"/><circle cx="26" cy="16" r="6"/><circle cx="38" cy="20" r="5"/><path d="M6 36c2-8 14-8 16 0zM16 36c2-10 18-10 20 0z"/><circle cx="42" cy="34" r="7"/><path d="M39 34l2 2 4-4" stroke="#fff" stroke-width="2" fill="none"/></svg><span>4.5/5.0 Customer<br>Service Rating</span></div>
  </div>
  <div class="btn" style="left:395px;top:356px;width:178px;height:44px">Read More</div>
</section>

<!-- resources -->
<h2 class="abs script res-title">Resources</h2>
<p class="abs res-copy">Lorem Ipsum is simply dummy text of the printing and typesetting industry. Lorem Ipsum has been the industry's standard dummy text ever since the 1500s, when an unknown printer took a galley of type and scrambled it to make a type specimen book. It has survived not only five centuries, but also the leap into electronic typesetting, remaining essentially unchanged.Lorem Ipsum is simply dummy text of the printing and typesetting industry. Lorem Ipsum has been the industry's standard dummy text ever since the 1500s, when an unknown</p>
<div class="btn" style="left:113px;top:2822px;width:176px;height:49px">Read More</div>
<div class="abs" style="left:658px;top:2514px;width:362px;height:362px;border-radius:50%;border:5px solid var(--gold);background:linear-gradient(135deg,#cfd8df,#8a7866 50%,#3e5566)" role="img" aria-label="Three colleagues discussing over a tablet"></div>

<!-- upcoming sales -->
<div class="upcoming-band"></div>
<h2 class="abs script" style="left:111px;top:3048px;font-size:56px">Upcoming Sales</h2>
<svg class="abs" style="left:930px;top:3080px" width="30" height="30" viewBox="0 0 30 30" fill="none" stroke="#c99a33" stroke-width="2.5"><path d="M24 15H6M13 8l-7 7 7 7"/></svg>
<svg class="abs" style="left:979px;top:3078px" width="62" height="36" viewBox="0 0 62 36" fill="none" stroke="#c99a33" stroke-width="2.5"><rect x="1.5" y="1.5" width="59" height="33" rx="2"/><path d="M20 18h22M35 11l7 7-7 7"/></svg>

<div class="sale-card" style="left:111px;width:424px">
  <div class="sale-photo" style="background:linear-gradient(180deg,#8fb6dd 0%,#a9a39a 50%,#5f7a3e 100%)" role="img" aria-label="Brick two-storey home with flower garden"></div>
  <p>Lorem Ipsum is simply dummyLorem Ipsum is simply dummy</p>
  <a>Get Started <svg width="26" height="12" viewBox="0 0 26 12" fill="none" stroke="#c99a33" stroke-width="2"><path d="M1 6h23M19 1l5 5-5 5"/></svg></a>
</div>
<div class="sale-card" style="left:561px;width:430px">
  <div class="sale-photo" style="background:linear-gradient(180deg,#e6eef2 0%,#b9ada0 55%,#4f7438 100%)" role="img" aria-label="Modern white and wood house with lawn"></div>
  <p>Lorem Ipsum is simply dummyLorem Ipsum is simply dummy</p>
  <a>Get Started <svg width="26" height="12" viewBox="0 0 26 12" fill="none" stroke="#c99a33" stroke-width="2"><path d="M1 6h23M19 1l5 5-5 5"/></svg></a>
</div>
<div class="sale-card" style="left:1022px;width:430px">
  <div class="sale-photo" style="background:linear-gradient(180deg,#e8e2d8 0%,#c7b49a 55%,#6d5a44 100%)" role="img" aria-label="Contemporary house with open patio"></div>
  <p>Lorem Ipsum is simply dummyLorem Ipsum is simply dummy</p>
  <a>Get Started <svg width="26" height="12" viewBox="0 0 26 12" fill="none" stroke="#c99a33" stroke-width="2"><path d="M1 6h23M19 1l5 5-5 5"/></svg></a>
</div>
<svg class="abs" style="left:0;top:3540px" width="1200" height="70" viewBox="0 0 1200 70"><path d="M0 20 Q600 80 1200 20 V70 H0Z" fill="#fff"/><path d="M40 22 Q600 78 1160 22" stroke="#c99a33" stroke-width="5" fill="none"/></svg>

<!-- faq -->
<h2 class="section-title script" style="top:3676px">Frequently Asked Question</h2>
<div class="faq-item" style="top:3775px"><div class="faq-q">Lorem Ipsum is simply dummy text of the printing and typesetting industry<span class="sign">+</span></div></div>
<div class="faq-item" style="top:3835px"><div class="faq-q">Lorem Ipsum is simply dummy text of the printing and typesetting industry<span class="sign">+</span></div></div>
<div class="faq-item" style="top:3895px"><div class="faq-q">Lorem Ipsum is simply dummy text of the printing and typesetting industry<span class="sign">+</span></div></div>
<div class="faq-item" style="top:3955px"><div class="faq-q">Lorem Ipsum is simply dummy text of the printing and typesetting industry<span class="sign">–</span></div>
  <p class="faq-a">Lorem Ipsum is simply dummy text of the printing and typesetting industry. Lorem Ipsum has been the industry's standard dummy text ever since the 1500s, when an unknown printer took a galley of type and scrambled it to make a type specimen book.</p></div>
<div class="faq-item" style="top:4093px"><div class="faq-q">Lorem Ipsum is simply dummy text of the printing and typesetting industry<span class="sign">+</span></div></div>

<!-- footer -->
<svg class="abs" style="left:0;top:4240px" width="1200" height="60" viewBox="0 0 1200 60"><path d="M0 56 Q600 -6 1200 56 V60 H0Z" fill="#0b0b0b"/><path d="M40 40 Q600 -4 1160 40" stroke="#c99a33" stroke-width="4" fill="none"/></svg>
<footer class="footer">
  <div class="foot-brand">Bright Haven<br>Estate Sales</div>
  <div class="foot-col">
    <h4 style="left:414px">Navigation</h4>
    <div class="foot-link" style="left:414px;top:94px">Services</div>
    <div class="foot-link" style="left:414px;top:122px">Upcoming Sales</div>
    <div class="foot-link" style="left:414px;top:150px">About Us</div>
    <div class="foot-link" style="left:414px;top:178px">FAQs</div>
    <div class="foot-link" style="left:414px;top:206px">Resources</div>
  </div>
  <div class="foot-col">
    <h4 style="left:637px">Contact Info</h4>
    <svg class="abs" style="left:634px;top:95px" width="14" height="14" viewBox="0 0 24 24" fill="#fff"><path d="M6 2l4 4-2 3c1 3 4 6 7 7l3-2 4 4-3 4C10 22 2 14 2 5z"/></svg>
    <div class="foot-link" style="left:655px;top:94px">+1888 888 8888</div>
    <svg class="abs" style="left:632px;top:125px" width="16" height="12" viewBox="0 0 16 12" fill="none" stroke="#fff" stroke-width="1.5"><rect x="1" y="1" width="14" height="10"/><path d="M1 1l7 6 7-6"/></svg>
    <div class="foot-link" style="left:655px;top:122px;line-height:28px">info@brighthaven<br>estatesales.example</div>
    <svg class="abs" style="left:634px;top:176px" width="13" height="17" viewBox="0 0 13 17" fill="#fff"><path d="M6.5 0C3 0 0 3 0 6.5 0 11 6.5 17 6.5 17S13 11 13 6.5C13 3 10 0 6.5 0zm0 9a2.5 2.5 0 110-5 2.5 2.5 0 010 5z"/></svg>
    <div class="foot-link" style="left:655px;top:178px;line-height:28px">1791 Lorem Ipsum<br>Lorem lorem<br>lorem ipsum</div>
  </div>
  <div class="abs subscribe">
    <h4>Subscribe</h4>
    <p>Are you interested in following us for Getting Sale Update website</p>
    <div class="sub-input">Your Email Address<svg width="28" height="28" viewBox="0 0 28 28"><circle cx="14" cy="14" r="13" fill="#fff"/><path d="M8 14h12M15 9l5 5-5 5" stroke="#1d1d1d" stroke-width="2" fill="none"/></svg></div>
  </div>
  <div class="foot-rule"></div>
  <div class="social" style="left:112px"></div>
  <div class="social" style="left:166px"></div>
  <div class="social" style="left:217px"></div>
  <div class="copyright">© 2024 Bright Haven Estate Sales I All Rights Reserved</div>
</footer>

</body>
</html>
```